Chic streamline modern edgy! Tamvexcurl.com

I need a website built for my personal business. I am a hair stylist and I would like a crisp website that works well, is sleek, easy to use, and allows my clients to navigate through Services and pay deposits for services listed.

My logo is somewhat of a full moon, so my theme is nocturnal.

My information can be found at bookmiro.com/tamvexcurl

Target Market(s)

Women ages 25-55 who are looking for luxury hair extension services

Industry/Entity Type

Hair And Beauty

Number of Pages Required

1 page

Colors
474747
919191
d3d3d3
000000

Requirements
Must have
• Location map, quorba link embedded for deposits, contact box, bio, faq/policies, menu of services, hours of availability by appointment only .
Nice to have
• An interactive calander where I could post dates that I am available, preferred providers for other beauty services where i could list other websites for make up and other beauty related referrals. a bridal tab would be nice to offer information about bridal services and policies.

```html
<!DOCTYPE html>
<html lang="en">
<head>
<meta charset="utf-8">
<title>Tamvexcurl.com — Testimonials &amp; Gallery</title>
<link rel="stylesheet" href="https://fonts.googleapis.com/css2?family=Roboto:ital,wght@0,300;0,400;0,900;1,300&display=swap">
<style>
  :root {
    --night: #000000;
    --charcoal: #474747;
    --ash: #919191;
    --mist: #d3d3d3;
    --title-grey: #7a7a7a;
    --quote-grey: #5c5c5c;
    --text-light: #e6e6e6;
    --white: #ffffff;
  }
  * { box-sizing: border-box; margin: 0; padding: 0; }
  html, body { width: 982px; height: 1200px; overflow: hidden; background: var(--night); }
  body { font-family: 'Roboto', sans-serif; position: relative; }

  .testimonials {
    position: absolute; left: 0; top: 0; width: 982px; height: 552px;
    background: var(--night); overflow: hidden;
  }
  .testimonials__backdrop {
    position: absolute; inset: 0;
    background:
      radial-gradient(ellipse 60px 50px at 491px 540px, #3a3a3a 0%, rgba(40,40,40,0.6) 60%, transparent 100%),
      radial-gradient(ellipse 110px 170px at 440px 250px, rgba(85,85,85,0.45) 0%, transparent 100%),
      radial-gradient(ellipse 120px 180px at 560px 230px, rgba(75,75,75,0.4) 0%, transparent 100%),
      radial-gradient(ellipse 250px 290px at 491px 260px, #2a2a2a 0%, #1a1a1a 45%, #0a0a0a 80%, #000 100%);
  }
  .section-title {
    position: absolute; left: 0; width: 100%; text-align: center;
    font-weight: 400; font-size: 47px; letter-spacing: 0.5px; line-height: 1;
  }
  .testimonials .section-title { top: 37px; color: var(--title-grey); }
  .section-rule {
    position: absolute; left: 292px; width: 400px; height: 1px;
    background: linear-gradient(90deg, transparent, var(--ash), transparent);
  }
  .testimonials .section-rule { top: 88px; }

  .client-avatar {
    position: absolute; left: 427px; top: 133px; width: 128px; height: 128px;
    border-radius: 50%; border: 1px solid var(--mist);
    background:
      radial-gradient(ellipse 30px 40px at 72px 72px, #7a6460 0%, rgba(90,70,66,0) 100%),
      linear-gradient(100deg, #1c1616 0%, #4a3a3a 35%, #2a2020 55%, #5a4644 75%, #1a1414 100%);
  }
  .quote-mark { position: absolute; top: 253px; width: 56px; height: 46px; }
  .quote-mark--open { left: 70px; }
  .quote-mark--close { left: 856px; }
  .quote-mark svg { width: 56px; height: 46px; display: block; }

  .testimonial__quote {
    position: absolute; left: 212px; top: 281px; width: 558px; text-align: center;
    font-style: italic; font-weight: 300; font-size: 17.2px; line-height: 34.5px; color: var(--text-light);
  }
  .testimonial__name {
    position: absolute; left: 0; top: 391px; width: 100%; text-align: center;
    font-size: 26px; font-weight: 400; color: var(--white); letter-spacing: 0.3px; line-height: 1.2;
  }
  .testimonial__date {
    position: absolute; left: 0; top: 425px; width: 100%; text-align: center;
    font-size: 13px; font-weight: 400; color: var(--mist);
  }

  .slider-nav { position: absolute; left: 455px; width: 72px; height: 30px; }
  .testimonials .slider-nav { top: 479px; }
  .gallery .slider-nav { top: 585px; }
  .slider-nav svg { width: 72px; height: 30px; display: block; }

  .gallery {
    position: absolute; left: 0; top: 552px; width: 982px; height: 648px;
    background: var(--charcoal);
  }
  .gallery .section-title { top: 38px; color: var(--night); }
  .gallery .section-rule { top: 90px; }
  .gallery__item {
    position: absolute; width: 194px; height: 194px; border-radius: 50%;
    border: 1px solid var(--mist);
    box-shadow: inset 0 0 22px rgba(255,255,255,0.25);
  }
  .tone-a { background:
      radial-gradient(ellipse 34px 44px at 50% 42%, #cfcfcf 0%, rgba(200,200,200,0) 100%),
      radial-gradient(ellipse 80px 95px at 50% 50%, #5a5a5a 0%, #7c7c7c 60%, rgba(220,220,220,0) 100%),
      radial-gradient(circle at 50% 50%, #e2e2e2 0%, #d0d0d0 70%, #9a9a9a 100%); }
  .tone-b { background:
      radial-gradient(ellipse 32px 44px at 50% 40%, #5a3a28 0%, rgba(90,58,40,0) 100%),
      radial-gradient(ellipse 78px 92px at 50% 48%, #c8a06a 0%, #a87e4c 65%, rgba(160,120,70,0) 100%),
      linear-gradient(180deg, #e8e2d8 0%, #cbbfae 55%, #3f4a5e 100%); }
  .tone-c { background:
      radial-gradient(ellipse 32px 44px at 45% 42%, #7a7a7a 0%, rgba(120,120,120,0) 100%),
      radial-gradient(ellipse 82px 96px at 45% 48%, #262626 0%, #3a3a3a 60%, rgba(200,200,200,0) 100%),
      radial-gradient(circle at 50% 50%, #bdbdbd 0%, #9e9e9e 75%, #6e6e6e 100%); }
  .tone-d { background:
      radial-gradient(ellipse 34px 44px at 55% 46%, #8a8a8a 0%, rgba(130,130,130,0) 100%),
      radial-gradient(ellipse 88px 96px at 45% 50%, #1a1a1a 0%, #2a2a2a 60%, rgba(180,180,180,0) 100%),
      radial-gradient(circle at 50% 50%, #a8a8a8 0%, #8a8a8a 75%, #555 100%); }
  .tone-e { background:
      radial-gradient(ellipse 36px 48px at 50% 52%, #6c6c6c 0%, rgba(100,100,100,0) 100%),
      radial-gradient(ellipse 90px 100px at 50% 48%, #141414 0%, #1e1e1e 65%, rgba(90,90,90,0) 100%),
      linear-gradient(180deg, #6a6a6a 0%, #4c4c4c 80%, #cfcfcf 100%); }
  .tone-f { background:
      radial-gradient(ellipse 30px 40px at 50% 40%, #7c7c7c 0%, rgba(120,120,120,0) 100%),
      radial-gradient(ellipse 70px 100px at 50% 55%, #202020 0%, #2e2e2e 60%, rgba(230,230,230,0) 100%),
      radial-gradient(circle at 50% 50%, #f2f2f2 0%, #e2e2e2 70%, #b8b8b8 100%); }
  .tone-g { background:
      radial-gradient(ellipse 32px 42px at 50% 48%, #7a7a7a 0%, rgba(120,120,120,0) 100%),
      radial-gradient(ellipse 84px 88px at 50% 48%, #101010 0%, #1e1e1e 65%, rgba(240,240,240,0) 100%),
      radial-gradient(circle at 50% 50%, #f4f4f4 0%, #e6e6e6 70%, #bcbcbc 100%); }
  .tone-h { background:
      radial-gradient(ellipse 28px 40px at 58% 50%, #6e6e6e 0%, rgba(110,110,110,0) 100%),
      radial-gradient(ellipse 86px 100px at 50% 50%, #121212 0%, #262626 65%, rgba(200,200,200,0) 100%),
      radial-gradient(circle at 50% 50%, #cfcfcf 0%, #b4b4b4 70%, #7a7a7a 100%); }
</style>
</head>
<body>

<section class="testimonials">
  <div class="testimonials__backdrop" role="img" aria-label="Dark photograph of a woman's sleek styled hair seen from behind"></div>
  <h2 class="section-title">TESTIMONIALS</h2>
  <div class="section-rule"></div>

  <div class="client-avatar" role="img" aria-label="Portrait of the client with a sleek side-swept bob"></div>

  <span class="quote-mark quote-mark--open" aria-hidden="true">
    <svg viewBox="0 0 56 46"><path fill="#5c5c5c" d="M2 46 V26 C2 10 10 2 24 0 V9 C16 11 13 16 13 21 H24 V46 Z M32 46 V26 C32 10 40 2 54 0 V9 C46 11 43 16 43 21 H54 V46 Z"/></svg>
  </span>
  <span class="quote-mark quote-mark--close" aria-hidden="true">
    <svg viewBox="0 0 56 46"><path fill="#5c5c5c" d="M2 0 V20 C2 36 10 44 24 46 V37 C16 35 13 30 13 25 H24 V0 Z M32 0 V20 C32 36 40 44 54 46 V37 C46 35 43 30 43 25 H54 V0 Z"/></svg>
  </span>

  <p class="testimonial__quote">"He works with passion. You can actually see it in his eyes you're in his chair. He cares about the health of you hair as well as the look. You can't beat quality service like his. You just can't! I look and feel FABULOUS!!!????"</p>
  <p class="testimonial__name">Dana&nbsp; M.</p>
  <p class="testimonial__date">12th August, 2015</p>

  <nav class="slider-nav" aria-label="Testimonial navigation">
    <svg viewBox="0 0 72 30">
      <circle cx="15" cy="15" r="14" fill="#3a3a3a" stroke="#5e5e5e"/>
      <path d="M17 9 l-6 6 6 6 M22 9 l-6 6 6 6" fill="none" stroke="#9a9a9a" stroke-width="1.6"/>
      <circle cx="58" cy="15" r="14" fill="#bdbdbd" stroke="#e0e0e0"/>
      <path d="M51 9 l6 6 -6 6 M56 9 l6 6 -6 6" fill="none" stroke="#1a1a1a" stroke-width="1.6"/>
    </svg>
  </nav>
</section>

<section class="gallery">
  <h2 class="section-title">GALLERY</h2>
  <div class="section-rule"></div>

  <div class="gallery__item tone-a" style="left:70px; top:133px" role="img" aria-label="Black and white photo of long curly styled hair"></div>
  <div class="gallery__item tone-b" style="left:286px; top:133px" role="img" aria-label="Colour photo of long honey blonde extensions"></div>
  <div class="gallery__item tone-c" style="left:502px; top:133px" role="img" aria-label="Black and white photo of a smooth shoulder-length style"></div>
  <div class="gallery__item tone-d" style="left:718px; top:133px" role="img" aria-label="Black and white photo of glamorous voluminous curls"></div>
  <div class="gallery__item tone-e" style="left:70px; top:349px" role="img" aria-label="Black and white photo of soft waved long hair"></div>
  <div class="gallery__item tone-f" style="left:286px; top:349px" role="img" aria-label="Black and white photo of long straight extensions"></div>
  <div class="gallery__item tone-g" style="left:502px; top:349px" role="img" aria-label="Black and white photo of a curly bob"></div>
  <div class="gallery__item tone-h" style="left:718px; top:349px" role="img" aria-label="Black and white photo of a sleek asymmetric bob"></div>

  <nav class="slider-nav" aria-label="Gallery navigation">
    <svg viewBox="0 0 72 30">
      <circle cx="15" cy="15" r="14" fill="#2e2e2e" stroke="#5e5e5e"/>
      <path d="M17 9 l-6 6 6 6 M22 9 l-6 6 6 6" fill="none" stroke="#9a9a9a" stroke-width="1.6"/>
      <circle cx="58" cy="15" r="14" fill="#bdbdbd" stroke="#e0e0e0"/>
      <path d="M51 9 l6 6 -6 6 M56 9 l6 6 -6 6" fill="none" stroke="#1a1a1a" stroke-width="1.6"/>
    </svg>
  </nav>
</section>

</body>
</html>
```